3 x DIN A4 Flyer, Vorder- und Rückseite
Zielgruppe
Handwerksunternehmen
Aufgabenstellung
Wir benötigen 3 Werbeflyer die in Zeitschriften beigelegt werden. Jeweils DIN A4, Vorderseite beschreibt das Produkt, Rückseite kann zur Bestellung mittels Faxantwort benutzt werden. Profibilder und Text wird vollständig geliefert.

```html
<!DOCTYPE html>
<html lang="de">
<head>
<meta charset="utf-8">
<title>Kundenstopper – Flyer</title>
<link rel="stylesheet" href="https://fonts.googleapis.com/css2?family=Open+Sans:wght@400;600;700&display=swap">
<style>
  :root {
    --page-bg: #ffffff;
    --sky-top: #d6ecf9;
    --sky-mid: #b7dcf3;
    --sky-low: #cde6f6;
    --band: #a9d4ef;
    --band-light: #e7f4fc;
    --navy: #233f8c;
    --ink: #1f3470;
    --orange: #ee8a1f;
    --panel: rgba(255,255,255,0.45);
    --silver-a: #dfe3e8;
    --silver-b: #9ea7b3;
    --measure: #2f4fa3;
  }
  * { box-sizing: border-box; margin: 0; padding: 0; }
  html, body { width: 1200px; height: 800px; overflow: hidden; background: var(--page-bg); }
  body { font-family: "Open Sans", Arial, sans-serif; color: var(--ink); }

  .flyer {
    position: absolute; left: 310px; top: 0; width: 580px; height: 800px; overflow: hidden;
    background: linear-gradient(180deg, var(--sky-top) 0%, var(--sky-mid) 35%, var(--sky-low) 70%, var(--band-light) 100%);
  }
  .band { position: absolute; transform-origin: left center; }
  .band--title { left: -20px; top: 70px; width: 640px; height: 62px; background: var(--band); transform: rotate(-4deg); }
  .band--claim { left: -20px; top: 132px; width: 640px; height: 78px; background: linear-gradient(90deg, rgba(255,255,255,0.35), rgba(169,212,239,0.9)); transform: rotate(-4deg); }

  .title { position: absolute; left: 50px; top: 78px; font-size: 32px; font-weight: 700; color: var(--navy); transform: rotate(-3deg); letter-spacing: -0.3px; }
  .claim { position: absolute; right: 22px; top: 124px; text-align: right; font-size: 28px; line-height: 40px; font-weight: 700; color: var(--orange); transform: rotate(-3deg); }

  .product-photo { position: absolute; left: 73px; top: 164px; width: 164px; height: 458px; }

  .format-note { position: absolute; left: 145px; top: 330px; font-size: 10px; line-height: 13px; font-weight: 600; color: var(--ink); }
  .format-note p + p { margin-top: 12px; }

  .uses-panel {
    position: absolute; left: 337px; top: 270px; width: 228px; height: 238px;
    background: var(--panel); transform: rotate(-7deg);
  }
  .uses { position: absolute; left: 350px; top: 280px; width: 220px; transform: rotate(-7deg); transform-origin: left top; }
  .uses__intro { font-size: 9.5px; line-height: 20px; font-weight: 700; color: var(--ink); }
  .uses__list { list-style: none; margin-top: 12px; margin-left: 18px; }
  .uses__list li { display: flex; align-items: center; gap: 14px; font-size: 11px; height: 25px; color: var(--navy); }
  .uses__list svg { width: 14px; height: 10px; flex: none; }

  .price-band {
    position: absolute; left: 20px; top: 530px; width: 230px; height: 44px;
    background: linear-gradient(90deg, var(--band), var(--band-light)); transform: rotate(-2deg);
  }
  .price { position: absolute; left: 72px; top: 531px; display: flex; align-items: flex-start; gap: 6px; color: var(--navy); }
  .price__amount { font-size: 28px; font-weight: 700; }
  .price__unit { font-size: 10px; font-weight: 700; line-height: 11px; margin-top: 12px; }
  .price__unit small { display: block; font-size: 6px; }

  .details { position: absolute; left: 197px; top: 592px; width: 360px; }
  .details__heading { font-size: 9.5px; font-weight: 700; color: var(--ink); margin-bottom: 14px; }
  .details__list { list-style: none; }
  .details__list li { position: relative; padding-left: 13px; font-size: 8.5px; line-height: 12.8px; color: var(--ink); }
  .details__list li::before { content: "+"; position: absolute; left: 0; top: 0; font-weight: 700; color: var(--navy); }

  .legal { position: absolute; left: 20px; right: 20px; top: 729px; text-align: center; font-size: 7.5px; line-height: 11px; color: var(--ink); }
  .legal__company { margin-top: 9px; }
</style>
</head>
<body>
<main class="flyer">
  <div class="band band--title"></div>
  <div class="band band--claim"></div>

  <h1 class="title">Kundenstopper</h1>
  <p class="claim">clever werben<br>auf der Baustelle!</p>

  <svg class="product-photo" role="img" aria-label="Foto eines silbernen, aufgeklappten Kundenstoppers mit Klemmrahmen" viewBox="0 0 164 458">
    <defs>
      <linearGradient id="silver" x1="0" y1="0" x2="1" y2="1">
        <stop offset="0" stop-color="var(--silver-a)"/>
        <stop offset="1" stop-color="var(--silver-b)"/>
      </linearGradient>
    </defs>
    <rect width="164" height="458" rx="6" fill="url(#silver)" opacity="0.85"/>
    <line x1="40" y1="290" x2="160" y2="60" stroke="var(--measure)" stroke-width="1.2"/>
  </svg>

  <div class="format-note">
    <p>Plakatformat!<br>DIN A1 (60cm x 85cm)</p>
    <p>Ständermaße! (121cm x 66cm)</p>
  </div>

  <div class="uses-panel"></div>
  <section class="uses">
    <p class="uses__intro">Kundenstopper / Werbeständer /<br>Gehwegaufsteller / Bockständer<br>für Innen und Außen!</p>
    <ul class="uses__list">
      <li><svg viewBox="0 0 14 10"><path d="M1 5h11M8 1l4 4-4 4" fill="none" stroke="var(--navy)" stroke-width="1.6"/></svg>Messen</li>
      <li><svg viewBox="0 0 14 10"><path d="M1 5h11M8 1l4 4-4 4" fill="none" stroke="var(--navy)" stroke-width="1.6"/></svg>Aktionstage</li>
      <li><svg viewBox="0 0 14 10"><path d="M1 5h11M8 1l4 4-4 4" fill="none" stroke="var(--navy)" stroke-width="1.6"/></svg>Tag der offenen Tür</li>
      <li><svg viewBox="0 0 14 10"><path d="M1 5h11M8 1l4 4-4 4" fill="none" stroke="var(--navy)" stroke-width="1.6"/></svg>Gewerbeveranstaltungen</li>
      <li><svg viewBox="0 0 14 10"><path d="M1 5h11M8 1l4 4-4 4" fill="none" stroke="var(--navy)" stroke-width="1.6"/></svg>vor dem Betrieb</li>
    </ul>
  </section>

  <div class="price-band"></div>
  <p class="price"><span class="price__amount">39,–</span><span class="price__unit">EUR*<small>(netto)</small></span></p>

  <section class="details">
    <h2 class="details__heading">Produktdetails</h2>
    <ul class="details__list">
      <li>klappbares Standgestell</li>
      <li>2 aufmontierte Klemmrahmen mit 32 mm breitem Profil mit<br>übergroßer Antireflex-Schutzfolie</li>
      <li>Ecken auf Gehrung geschnitten</li>
      <li>verzinkte Stahlblechrückwand (einseitig beschichtet) und Antireflex-Schutzfolie</li>
      <li>beidseitig nutzbar</li>
    </ul>
  </section>

  <footer class="legal">
    <p>* Alle angegebenen Preise verstehen sich in Euro zzgl. der gesetzlichen geltenden Mehrwertsteuer von derzeit 19%.<br>
    Die Lieferung erfolgt ca.10 Tage nach Bestelleingang. Porto/Verpackung 12,90 Euro</p>
    <p class="legal__company">Kontorgesellschaft für Ladenbau und Tischlerei mbH · Lindenweg 8 · 80999 München · www.kltr-gmbh.de</p>
  </footer>
</main>
</body>
</html>
```